New eyelid plastic surgery office needs a business card design-Eyelid Surgery Partners of Brennor

I recently used SketchHarbor for my logo design and was very pleased with creativity and results. It was a difficult decision for me. Now I would like to create a business card based on this logo, which I will attach.

The text should be easily legible as some of my patients have difficulty seeing, but I would like a subtle, sophisticated artistry also evident to make the card memorable. Would like the card based on a similar color scheme as the logo but the inverse or other complementary colors may prove interesting

A good question was asked...my concern about my visually impaired patients was really my desire to avoid italicized or calligraphic type fonts that may be hard to read. Standard font size for a business card would be fine. Thanks!

Thank you so much for the great work so far. I wanted to give you my particular contact information to see if that would change the look of the cards. Martin Pellowby, MD Address: 2817 Larkmoor Avenue, Suite 205 Wilmington, NC 28517 Phone: 910-555-0183 Fax: 910-555-0184 Website: www.brennorlidclinic.example Please delete the email slot from the card. Thanks so much!

Reason: Last minute consideration. So many great revisions right now!

Plastic

```html
<!DOCTYPE html>
<html lang="en">
<head>
<meta charset="utf-8">
<title>Eyelid Surgery Partners of Brennor — Business Card</title>
<link rel="stylesheet" href="https://fonts.googleapis.com/css2?family=Arimo:wght@700&family=Tenor+Sans&display=swap">
<style>
  :root {
    --backdrop: #e9ecef;
    --card-white: #ffffff;
    --card-mist: #d9e3ef;
    --card-edge: #aebfd6;
    --brand-blue: #1c4f9c;
    --ink: #1a1a1a;
    --rule: #555a60;
    --swoosh: #c9ced6;
    --band-royal: #1d2fb8;
    --band-deep: #0d1a7a;
    --band-gold: #c9a233;
    --strip-steel: #3f73b8;
    --strip-light: #6f9bd6;
  }
  html, body {
    margin: 0;
    width: 1200px;
    height: 888px;
    overflow: hidden;
    background: var(--backdrop);
  }
  .card {
    position: absolute;
    left: 100px;
    top: 158px;
    width: 1000px;
    height: 572px;
    background: radial-gradient(ellipse at 45% 40%, var(--card-white) 35%, var(--card-mist) 80%, var(--card-edge) 100%);
    box-shadow: 0 10px 30px rgba(0,0,0,.25);
    overflow: hidden;
  }
  .card__swoosh {
    position: absolute;
    left: 0;
    top: 0;
    width: 820px;
    height: 572px;
  }
  .brand {
    position: absolute;
    left: 180px;
    top: 70px;
    width: 560px;
    margin: 0;
    font-family: "Tenor Sans", "Optima", sans-serif;
    font-weight: 400;
    color: var(--brand-blue);
    text-align: center;
    line-height: 1;
  }
  .brand__main {
    display: block;
    font-size: 58px;
    letter-spacing: 1px;
  }
  .brand__sub {
    display: block;
    margin-top: 8px;
    font-size: 30px;
    letter-spacing: 1px;
  }
  .contact {
    position: absolute;
    left: 70px;
    top: 290px;
    width: 640px;
    padding-left: 18px;
    border-left: 2px solid var(--rule);
    font-family: "Arimo", Arial, sans-serif;
    font-weight: 700;
    color: var(--ink);
  }
  .contact__label {
    margin: 0 0 14px;
    font-size: 17px;
  }
  .contact__name {
    margin: 0 0 14px 120px;
    font-size: 30px;
  }
  .contact__list {
    margin: 0;
    display: grid;
    grid-template-columns: 84px 1fr;
    row-gap: 4px;
    font-size: 17px;
  }
  .contact__list dt, .contact__list dd { margin: 0; }
  .contact__list dd::before { content: ": "; }
  .ornament-band {
    position: absolute;
    left: 820px;
    top: 0;
    width: 120px;
    height: 572px;
    background: linear-gradient(90deg, var(--band-deep), var(--band-royal) 45%, var(--band-gold) 50%, var(--band-royal) 55%, var(--band-deep));
  }
  .edge-strip {
    position: absolute;
    left: 940px;
    top: 0;
    width: 60px;
    height: 572px;
    background: linear-gradient(90deg, var(--strip-steel), var(--strip-light));
  }
</style>
</head>
<body>
  <section class="card" aria-label="Business card">
    <svg class="card__swoosh" viewBox="0 0 820 572" aria-hidden="true">
      <path d="M0 520 C 220 360, 520 300, 700 330 C 560 330, 300 400, 0 560 Z" fill="var(--swoosh)" opacity=".5"/>
      <path d="M60 572 C 260 470, 500 430, 680 440" fill="none" stroke="var(--swoosh)" stroke-width="3" opacity=".7"/>
    </svg>

    <h1 class="brand">
      <span class="brand__main">EYELID SURGERY</span>
      <span class="brand__sub">PARTNERS OF BRENNOR</span>
    </h1>

    <div class="contact">
      <p class="contact__label">Contact :</p>
      <p class="contact__name">Martin Pellowby, MD</p>
      <dl class="contact__list">
        <dt>Address</dt><dd>2817 Larkmoor Avenue, Suite 205 Wilmington, NC 28517</dd>
        <dt>Phone</dt><dd>910 - 555 - 0183</dd>
        <dt>Fax</dt><dd>910 - 555 - 0184</dd>
        <dt>web</dt><dd>www.brennorlidclinic.example</dd>
      </dl>
    </div>

    <div class="ornament-band" role="img" aria-label="Vertical band of gold floral ornaments on royal blue"></div>
    <div class="edge-strip"></div>
  </section>
</body>
</html>
```